Consumer Protection Law Firm Needs a New Website

We need a new website for our law firm. We practice consumer protection law, with an emphasis on class actions. In particular, we serve consumers who are harassed by telemarketers, debt collectors, abusive companies, and financial criminals. In short, we sue big companies that do bad things to lots of people.

The lawyer is Tomas Fenwald. Current website is available through www.FenwaldLegal.example. Some logo files are attached.

Prefer designs that use the colors black, red, and white, per the logo. Also prefer clean, lightweight HTML5/CSS3 design rather than Wordpress. Finally, single-page type design preferred over multi-page, but flexible.

I have some limited familiarity with HTML and CSS, particularly Bootstrap, so a Bootstrap type design that I can modify myself would be ideal.

Target Market(s)

Consumers with cellular telephones.

Industry/Entity Type

Law Firm

Coding

Coded - Design and coding required

Number of Pages Required

1 page

Requirements
Must have
• - Mobile friendly, preferably without requiring separate design. In other words, a framework like Bootstrap is preferred.
• - Contact Form
• - A section for recent results
• - A section for a picture and bio of Tomas Fenwald, Esq.
Nice to have
• - Animated elements that count-up and populate with numbers for things like:
• * X dollars recovered for consumers.
• * Y clients represented
• * Over Z lawsuits filed for consumers

```html
<!DOCTYPE html>
<html lang="en">
<head>
<meta charset="utf-8">
<title>Fenwald Law – Consumer Advocates</title>
<link href="https://fonts.googleapis.com/css2?family=Cinzel:wght@400;700&family=Open+Sans:wght@400;600&display=swap" rel="stylesheet">
<style>
:root{
  --red:#b5123a;
  --red-dark:#8f0d2d;
  --ink:#222;
  --text:#555;
  --muted:#777;
  --line:#e3e3e3;
  --grey-band:#f1f1f1;
  --footer:#333;
  --footer-bottom:#262626;
  --ring-track:#dde3e8;
  --ring-dark:#454545;
}
*{box-sizing:border-box;margin:0;padding:0}
html,body{width:1200px;height:2579px;overflow:hidden;background:#fff}
body{font-family:"Open Sans",Arial,sans-serif;color:var(--text);position:relative}
.serif{font-family:"Cinzel",Georgia,serif}
.abs{position:absolute}

/* header */
.site-header{position:absolute;left:0;top:0;width:1200px;height:108px;border-bottom:1px solid var(--line)}
.brand{position:absolute;left:98px;top:34px;display:flex;align-items:center;gap:10px}
.brand-mark{width:34px;height:34px;background:var(--red)}
.brand-name{font-family:"Cinzel",Georgia,serif;font-size:25px;line-height:1;color:var(--ink);font-weight:700;letter-spacing:.5px}
.brand-tag{font-family:"Cinzel",Georgia,serif;font-size:11px;letter-spacing:3px;color:var(--ink);margin-top:3px;font-weight:700}
.call{position:absolute;left:862px;top:34px;display:flex;align-items:center;gap:10px;font-size:12px;color:var(--muted)}
.call-icon{width:40px;height:40px;border:2px solid var(--red);border-radius:50%;display:flex;align-items:center;justify-content:center}
.call strong{color:var(--red);font-weight:600;font-size:14px}

/* nav */
.main-nav{position:absolute;left:98px;top:108px;width:1004px;height:59px;display:flex;justify-content:space-between;align-items:center;font-family:"Cinzel",Georgia,serif;font-size:12px;color:var(--ink)}
.main-nav a{color:inherit;text-decoration:none;padding:0 16px}
.main-nav a.active{background:var(--red);color:#fff;height:59px;line-height:59px;width:101px;text-align:center;padding:0}
.main-nav a:last-child{padding-right:0}

/* hero */
.hero{position:absolute;left:0;top:167px;width:1200px;height:521px;background:linear-gradient(100deg,#c9c6c0 0%,#8a7a6c 35%,#4e3427 65%,#6a4a36 100%)}
.hero-arrows{position:absolute;left:98px;top:425px;color:#fff;font-size:40px;opacity:.8}
.hero-panel{position:absolute;left:734px;top:234px;width:366px;height:393px;background:rgba(25,25,25,.82);padding:22px 21px}
.hero-panel h2{color:#fff;font-weight:400;font-size:20px;line-height:1.2}
.hero-panel h2 span{display:block;font-size:32px}
.hero-panel p{color:#eee;font-style:italic;font-size:11.5px;line-height:1.6;margin-top:8px}
.field{display:block;width:324px;height:36px;background:#fff;border-radius:3px;margin-top:14px;font-size:11px;color:#999;line-height:36px;padding-left:14px}
.hero-panel .field:first-of-type{margin-top:20px}
.cta{display:block;width:324px;height:40px;background:var(--red);color:#fff;text-align:center;line-height:40px;font-family:"Cinzel",Georgia,serif;font-size:13px;margin-top:16px;border-radius:2px}

/* section heads */
.sec-title{position:absolute;left:0;width:1200px;text-align:center;font-family:"Cinzel",Georgia,serif;font-size:27px;color:var(--ink)}
.sec-sub{position:absolute;left:0;width:1200px;text-align:center;font-size:12.5px;color:var(--muted)}

/* services */
.services{position:absolute;left:98px;top:810px;width:1004px;height:184px;display:flex;border-bottom:1px solid var(--line)}
.service{flex:1;text-align:center;border-right:1px solid var(--line);padding:0 10px}
.service:last-child{border-right:0}
.svc-icon{width:48px;height:48px;border:1.5px solid var(--red);border-radius:4px;margin:6px auto 0;display:flex;align-items:center;justify-content:center}
.service h3{font-weight:400;font-size:14px;color:var(--red);margin-top:16px}
.service p{font-size:10.5px;line-height:1.75;color:var(--muted);margin-top:6px}

/* counters */
.stat{position:absolute;top:1129px;width:360px;text-align:center}
.stat svg{display:block;margin:0 auto}
.stat-num{position:absolute;left:0;top:44px;width:360px;text-align:center;font-family:"Cinzel",Georgia,serif;font-size:38px;color:var(--ink)}
.stat-num small{font-size:20px}
.stat-letter{font-family:"Cinzel",Georgia,serif;font-size:22px;color:var(--ink);margin-top:4px}
.stat-cap{font-family:"Cinzel",Georgia,serif;font-size:14px;letter-spacing:.5px;color:var(--ring-dark);margin-top:-2px}
.stat-cap.red{color:var(--red);font-weight:700}

/* practice areas */
.practice{position:absolute;left:0;top:1375px;width:1200px;height:427px;background:var(--grey-band)}
.practice h2{position:absolute;left:98px;top:42px;font-family:"Cinzel",Georgia,serif;font-size:26px;font-weight:400;color:var(--ink)}
.area{position:absolute;width:470px}
.area h3{font-weight:400;font-size:14px;color:var(--red);display:flex;align-items:center;gap:10px}
.area h3 i{width:13px;height:13px;border-radius:50%;background:var(--red);display:inline-block;position:relative}
.area h3 i::after{content:"";position:absolute;left:4px;top:3px;border-left:5px solid #fff;border-top:3.5px solid transparent;border-bottom:3.5px solid transparent}
.area p{font-size:10.5px;line-height:1.95;color:var(--text);margin-top:12px}

/* news */
.news-card{position:absolute;top:1936px;width:311px}
.news-img{width:311px;height:173px}
.news-card p{font-size:10.5px;line-height:1.9;color:var(--text);margin-top:20px}
.news-date{display:inline-block;width:113px;height:38px;line-height:38px;text-align:center;background:var(--red);color:#fff;font-family:"Cinzel",Georgia,serif;font-size:13px;margin-top:14px;box-shadow:0 2px 0 var(--red-dark)}

/* footer */
.site-footer{position:absolute;left:0;top:2283px;width:1200px;height:232px;background:var(--footer);color:#ccc}
.f-col{position:absolute;top:36px}
.f-col h4{font-family:"Cinzel",Georgia,serif;font-weight:400;font-size:14px;color:#fff;letter-spacing:.5px}
.f-col p{font-size:10.5px;line-height:1.85;margin-top:14px;color:#bbb}
.f-links{display:grid;grid-template-columns:110px 110px;font-family:"Cinzel",Georgia,serif;font-size:10.5px;margin-top:10px;row-gap:4px;color:#ccc}
.f-links span::before{content:"";display:inline-block;border-left:4px solid #ccc;border-top:3px solid transparent;border-bottom:3px solid transparent;margin-right:8px}
.f-contact{list-style:none;font-size:10.5px;line-height:1.8;margin-top:14px;color:#bbb}
.f-contact li{display:flex;gap:10px;margin-bottom:10px}
.search{display:flex;margin-top:16px}
.search-box{width:213px;height:34px;background:#fff}
.search-btn{width:34px;height:34px;background:var(--red);display:flex;align-items:center;justify-content:center}
.social{list-style:none;margin-top:20px}
.social li{display:flex;align-items:center;gap:16px;font-family:"Cinzel",Georgia,serif;font-size:10.5px;margin-bottom:12px;color:#ccc}
.social-box{width:32px;height:32px;border:1px solid #666}
.footer-bottom{position:absolute;left:0;top:2515px;width:1200px;height:64px;background:var(--footer-bottom);display:flex;align-items:center;justify-content:center;gap:12px;font-family:"Cinzel",Georgia,serif;font-size:12px;color:#ccc}
.footer-bottom .sq{width:26px;height:26px;background:#555}
</style>
</head>
<body>

<header class="site-header">
  <div class="brand">
    <div class="brand-mark"></div>
    <div>
      <div class="brand-name">FENWALD LAW</div>
      <div class="brand-tag">CONSUMER ADVOCATES</div>
    </div>
  </div>
  <div class="call">
    <div class="call-icon">
      <svg width="16" height="16" viewBox="0 0 24 24"><path fill="#b5123a" d="M6.6 10.8a15.1 15.1 0 006.6 6.6l2.2-2.2c.3-.3.7-.4 1-.2 1.1.4 2.3.6 3.6.6.6 0 1 .4 1 1V20c0 .6-.4 1-1 1A17 17 0 013 4c0-.6.4-1 1-1h3.5c.6 0 1 .4 1 1 0 1.3.2 2.5.6 3.6.1.3 0 .7-.2 1z"/></svg>
    </div>
    <span>CALL FENWALD : <strong>1.800.555.0142</strong></span>
  </div>
</header>

<nav class="main-nav">
  <a class="active">Home</a>
  <a>The Firm</a>
  <a>Practice Areas</a>
  <a>News</a>
  <a>FAQ</a>
  <a>Contact</a>
</nav>

<section class="hero" role="img" aria-label="Photo of attorney in a robe seated beside a stack of law books in an office">
  <div class="hero-arrows">&#x27E8; &#x27E9;</div>
</section>
<form class="hero-panel">
  <h2>Telephone harassment is a serious <span>violation of your rights.</span></h2>
  <p>Tomas Fenwald is a consumer lawyer dedicated to representing victims of telephone harassment and debt collector abuse. Have you been harassed? Don't delay, contact us today</p>
  <span class="field">First Name</span>
  <span class="field">Last Name</span>
  <span class="field">City state or Zip code</span>
  <span class="cta">GET YOUR FREE CONSULTATION</span>
</form>

<h2 class="sec-title" style="top:722px">Services</h2>
<p class="sec-sub" style="top:760px">Sed ut perspiciatis unde omnis iste natus error sit voluptatem accusantium doloremque laudantium,eaque ipsa quae ab...</p>

<div class="services">
  <div class="service">
    <div class="svc-icon"><svg width="20" height="20" viewBox="0 0 24 24"><path fill="#b5123a" d="M6.6 10.8a15.1 15.1 0 006.6 6.6l2.2-2.2c.3-.3.7-.4 1-.2 1.1.4 2.3.6 3.6.6.6 0 1 .4 1 1V20c0 .6-.4 1-1 1A17 17 0 013 4c0-.6.4-1 1-1h3.5c.6 0 1 .4 1 1 0 1.3.2 2.5.6 3.6.1.3 0 .7-.2 1z"/></svg></div>
    <h3>Telemarketers</h3>
    <p>Es simplemente el texto de relleno de las imprentas y archivos de textoha sido el simply ipsum texto...</p>
  </div>
  <div class="service">
    <div class="svc-icon"><svg width="22" height="18" viewBox="0 0 22 18"><rect x="1" y="1" width="20" height="16" rx="2" fill="none" stroke="#b5123a" stroke-width="2"/><rect x="1" y="5" width="20" height="3" fill="#b5123a"/><rect x="4" y="12" width="6" height="2" fill="#b5123a"/></svg></div>
    <h3>Debt Collectors</h3>
    <p>Es simplemente el texto de relleno de las imprentas y archivos de textoha sido el simply ipsum texto...</p>
  </div>
  <div class="service">
    <div class="svc-icon"><svg width="24" height="18" viewBox="0 0 24 18"><circle cx="12" cy="5" r="4" fill="#b5123a"/><circle cx="4.5" cy="7" r="3" fill="#b5123a"/><circle cx="19.5" cy="7" r="3" fill="#b5123a"/><path d="M5 18c0-5 3-8 7-8s7 3 7 8z" fill="#b5123a"/><path d="M0 17c0-3 2-6 4.5-6S8 13 8 14z M24 17c0-3-2-6-4.5-6S16 13 16 14z" fill="#b5123a"/></svg></div>
    <h3>Abusive Companies</h3>
    <p>Es simplemente el texto de relleno de las imprentas y archivos de textoha sido el simply ipsum texto...</p>
  </div>
  <div class="service">
    <div class="svc-icon" style="font-size:24px;color:var(--red);font-weight:600">$</div>
    <h3>Financial Criminals</h3>
    <p>Es simplemente el texto de relleno de las imprentas y archivos de textoha sido el simply ipsum texto...</p>
  </div>
</div>

<h2 class="sec-title" style="top:1033px">Count-up &amp; Populate</h2>
<p class="sec-sub" style="top:1073px">Sed ut perspiciatis unde omnis iste natus error sit voluptatem accusantium doloremque laudantium,eaque ipsa quae ab...</p>

<div class="stat" style="left:68px">
  <svg width="140" height="140" viewBox="0 0 140 140"><circle cx="70" cy="70" r="63" fill="none" stroke="var(--ring-track)" stroke-width="8"/><circle cx="70" cy="70" r="63" fill="none" stroke="var(--red)" stroke-width="8" stroke-dasharray="356.3 395.8" transform="rotate(-90 70 70)"/></svg>
  <div class="stat-num">90<small>%</small></div>
  <div class="stat-letter">X</div>
  <div class="stat-cap red">DOLLARS RECOVERED FOR CONSUMERS</div>
</div>
<div class="stat" style="left:437px">
  <svg width="140" height="140" viewBox="0 0 140 140"><circle cx="70" cy="70" r="63" fill="none" stroke="var(--ring-track)" stroke-width="8"/><circle cx="70" cy="70" r="63" fill="none" stroke="var(--ring-dark)" stroke-width="8" stroke-dasharray="356.3 395.8" transform="rotate(-90 70 70)"/></svg>
  <div class="stat-num">70<small>%</small></div>
  <div class="stat-letter">Y</div>
  <div class="stat-cap">CLIENTS REPRESENTED</div>
</div>
<div class="stat" style="left:822px">
  <svg width="140" height="140" viewBox="0 0 140 140"><circle cx="70" cy="70" r="63" fill="none" stroke="var(--ring-track)" stroke-width="8"/><circle cx="70" cy="70" r="63" fill="none" stroke="var(--ring-dark)" stroke-width="8" stroke-dasharray="356.3 395.8" transform="rotate(-90 70 70)"/></svg>
  <div class="stat-num">80<small>%</small></div>
  <div class="stat-letter">Z</div>
  <div class="stat-cap">LAWSUITS FILED FOR CONSUMERS</div>
</div>

<section class="practice">
  <h2>Practice Areas</h2>
  <div class="area" style="left:98px;top:110px">
    <h3><i></i>Telephone Harassment</h3>
    <p>Tomas Fenwald sues debt collectors, telemarketers, and spammers who violate the Telephone Consumer Protection Act ("TCPA"). Under the TCPA, violators an be held accountable and forced to pay heavy penalties to their victims. If you have been the subject of constant or abusive telephone calls, contact us for a free consultation...</p>
  </div>
  <div class="area" style="left:633px;top:110px">
    <h3><i></i>Text Message Spam</h3>
    <p>These days, advertisers are hard at work dreaming up new ways to get their brands in front of your eye. It is becoming ever more common for unscrupulous companies to abuse your cellular telephone with so-called "text spam." These companies frequently violate federal law. When they cross the line, Tomas Fenwald sues them and holds them accountable...</p>
  </div>
  <div class="area" style="left:98px;top:265px">
    <h3><i></i>Consumer Protection</h3>
    <p>Debt collectors are in the business of coercing consumers to pay money without regard for their legal rights. They call day and night, send letters, annoy, threaten, and abuse. Often times their practices are prohibited by federal or state law. Tomas Fenwald is versed in the law of unlawful debt collection practices, and holds offenders accountable in court. Contact us for a free consultation...</p>
  </div>
  <div class="area" style="left:633px;top:265px">
    <h3><i></i>Privacy</h3>
    <p>The law of privacy is relatively new and rapidly evolving. With the advent of the Internet, new privacy concerns emerge on an almost-daily basis. If you believe your privacy rights have been violated, contact us for a free consultation...</p>
  </div>
</section>

<h2 class="sec-title" style="top:1846px">Latest News</h2>
<p class="sec-sub" style="top:1885px">Sed ut perspiciatis unde omnis iste natus error sit voluptatem accusantium doloremque laudantium,eaque ipsa quae ab...</p>

<article class="news-card" style="left:98px">
  <div class="news-img" role="img" aria-label="Photo of a person in a suit signing a document at a desk" style="background:linear-gradient(135deg,#3a2a22,#8a6a55 55%,#e8e2da)"></div>
  <p>Consequuntur magni dolores eos qui ratione voluptatem nesciunt. Neque porro quisquam est, qui dolorem ipsum quia dolor sit amet, consectetur, adipisci velit, sed quia non numquam...</p>
  <span class="news-date">23 Jan 2016</span>
</article>
<article class="news-card" style="left:444px">
  <div class="news-img" role="img" aria-label="Photo of a glass office tower against a blue sky" style="background:linear-gradient(160deg,#2f6fd0,#6fa3e6 50%,#1d3f7a)"></div>
  <p>Consequuntur magni dolores eos qui ratione voluptatem nesciunt. Neque porro quisquam est, qui dolorem ipsum quia dolor sit amet, consectetur, adipisci velit, sed quia non numquam...</p>
  <span class="news-date">23 Jan 2016</span>
</article>
<article class="news-card" style="left:789px">
  <div class="news-img" role="img" aria-label="Photo of hands writing with a pen beside a calculator and coins" style="background:linear-gradient(135deg,#e9edf2,#c9d3de 50%,#8aa0b3)"></div>
  <p>Consequuntur magni dolores eos qui ratione voluptatem nesciunt. Neque porro quisquam est, qui dolorem ipsum quia dolor sit amet, consectetur, adipisci velit, sed quia non numquam...</p>
  <span class="news-date">23 Jan 2016</span>
</article>

<footer class="site-footer">
  <div class="f-col" style="left:98px;width:260px">
    <h4>ALL SITE PAGES</h4>
    <p>Below are listed all the pages included in this website, making it easier for you to navigate and find what you are looking for.</p>
    <div class="f-links"><span>Home</span><span>News</span><span>The Firm</span><span>FAQ</span><span>Practice Areas</span><span>Contact</span></div>
  </div>
  <div class="f-col" style="left:414px;width:220px">
    <h4>CONTACT US</h4>
    <ul class="f-contact">
      <li><span>&#9679;</span><span>Law Office of Tomas Fenwald, Esq.<br>4100 Harbor View Rd., Ste 210<br>Lakemont, FL 30000</span></li>
      <li><span>&#9679;</span><span>1.800.555.0188</span></li>
      <li><span>&#9993;</span><span>info@fenwaldlegal.example</span></li>
    </ul>
  </div>
  <div class="f-col" style="left:660px;width:260px">
    <h4>SEARCH THE SITE</h4>
    <p>Have a case you would like to discuss with us? Please feel free to call, email, or visit our office for a free consultation.</p>
    <div class="search">
      <div class="search-box"></div>
      <div class="search-btn"><svg width="14" height="14" viewBox="0 0 14 14"><circle cx="6" cy="6" r="4.2" fill="none" stroke="#fff" stroke-width="2"/><path d="M9 9l4 4" stroke="#fff" stroke-width="2"/></svg></div>
    </div>
  </div>
  <div class="f-col" style="left:980px;width:140px">
    <h4>FOLLOW WITH US</h4>
    <ul class="social">
      <li><span class="social-box"></span>Friendbook</li>
      <li><span class="social-box"></span>Chirper</li>
      <li><span class="social-box"></span>Circles Plus</li>
    </ul>
  </div>
</footer>
<div class="footer-bottom"><span class="sq"></span>Copyrights © fenwaldlaw . 2016 | Allrights Reserved.</div>

</body>
</html>
```